Business card design needed

I need a business card for my private practice. I would like to see the designs that use bright blue and white. I would like to see similar designs as to the card below:
http://blog.printmoss.com/2009/designing-a-business-card-with-pm-kt517-template.html
I would like to see the back of the card have room for appointment times. Thank you.

Industry/Entity Type
Business
Contact Information for Business Card
Tandem Wellbeing & Guidance Services
Fiona Marsh B.Psychology
Registered Psychologist
Building C, Level 3, 14 Wattle Crescent, Canberra, ACT 2601
T: (02) 6248 7315
F: (02) 6248 7390
info@tandemwellbeing.com.au
www.tandemwellbeing.com.au

```html
<!DOCTYPE html>
<html lang="en">
<head>
<meta charset="utf-8">
<title>Tandem Wellbeing &amp; Guidance Services – Business Card</title>
<link href="https://fonts.googleapis.com/css2?family=Source+Sans+3:wght@400;500;600&display=swap" rel="stylesheet">
<style>
  :root {
    --bg: #ececec;
    --card: #ffffff;
    --ink: #0b72bf;
    --sky: #aee0f8;
    --shadow: rgba(0, 0, 0, 0.55);
  }
  * { box-sizing: border-box; margin: 0; padding: 0; }
  html, body { width: 1200px; height: 900px; overflow: hidden; }
  body {
    background: var(--bg);
    font-family: "Source Sans 3", "Myriad Pro", Arial, sans-serif;
    color: var(--ink);
    position: relative;
  }
  .card {
    position: absolute;
    background: var(--card);
    box-shadow: 3px 3px 4px var(--shadow);
    overflow: hidden;
  }
  .card--front { left: 24px; top: 261px; width: 542px; height: 305px; }
  .card--back  { left: 632px; top: 261px; width: 545px; height: 307px; }

  .brand-mark {
    position: absolute;
    left: 18px; top: 127px;
    width: 50px; height: 50px;
    border-radius: 50%;
    background: var(--sky);
  }
  .brand-name {
    position: absolute;
    left: 80px; top: 116px; width: 168px;
    font-size: 20px; font-weight: 600; line-height: 24px;
    color: var(--ink);
  }

  .contact { position: absolute; left: 282px; top: 0; }
  .person-name {
    position: absolute; left: 0; top: 48px; white-space: nowrap;
    font-size: 19px; font-weight: 400;
  }
  .person-role {
    position: absolute; left: 0; top: 75px; white-space: nowrap;
    font-size: 15px; font-weight: 500;
  }
  .detail {
    position: absolute; white-space: nowrap;
    font-size: 14.5px; font-weight: 500; line-height: 18px;
  }
  .icon { position: absolute; fill: none; stroke: var(--ink); }

  .appointments-title {
    position: absolute; left: 228px; top: 64px;
    font-size: 15px; font-weight: 500; white-space: nowrap;
  }
  .appointment-line {
    position: absolute; left: 184px; width: 178px; height: 0;
    border-top: 1px dotted var(--ink);
  }
</style>
</head>
<body>

<section class="card card--front" aria-label="Business card front">
  <div class="brand-mark" aria-hidden="true"></div>
  <h1 class="brand-name">Tandem Wellbeing &amp; Guidance Services</h1>

  <div class="contact">
    <p class="person-name">Fiona Marsh | B. Psychology</p>
    <p class="person-role">Registered Psychologist</p>

    <svg class="icon" style="left:2px;top:109px" width="14" height="16" viewBox="0 0 14 16" aria-hidden="true">
      <path d="M7 15 C3 10 2 8 2 6 A5 5 0 0 1 12 6 C12 8 11 10 7 15Z" fill="var(--ink)" stroke="none"/>
      <circle cx="7" cy="6" r="1.8" fill="#fff" stroke="none"/>
    </svg>
    <p class="detail" style="left:24px;top:107px">Building C, Level 3<br>14 Wattle Crescent, Canberra<br>ACT 2601</p>

    <svg class="icon" style="left:1px;top:169px" width="16" height="16" viewBox="0 0 16 16" aria-hidden="true">
      <path d="M3 1 L6 1 L7 5 L5 6.5 C6 9 7.5 10.5 10 11.5 L11.5 9.5 L15 10.5 L15 14 C15 15 14 15.5 13 15 C7 13 3 9 1 3 C0.8 2 1.5 1 3 1Z" fill="var(--ink)" stroke="none"/>
    </svg>
    <p class="detail" style="left:24px;top:169px;font-size:14px">(02) 6248 7315</p>

    <svg class="icon" style="left:125px;top:167px" width="14" height="18" viewBox="0 0 14 18" aria-hidden="true">
      <path d="M1 1 H13 V12 L9 17 H1 Z" stroke-width="1.6"/>
      <path d="M8 11 H12 L8 16 Z" fill="var(--ink)" stroke="none"/>
    </svg>
    <p class="detail" style="left:146px;top:167px;font-size:14px">(02) 6248 7390</p>

    <svg class="icon" style="left:-4px;top:198px" width="24" height="16" viewBox="0 0 24 16" aria-hidden="true">
      <rect x="1" y="1" width="22" height="14" stroke-width="1.6"/>
      <path d="M1 1 L12 10 L23 1 M1 15 L9 8 M23 15 L15 8" stroke-width="1.4"/>
    </svg>
    <p class="detail" style="left:24px;top:197px">info@tandemwellbeing.com.au</p>

    <svg class="icon" style="left:-3px;top:228px" width="19" height="19" viewBox="0 0 19 19" aria-hidden="true" stroke-width="1">
      <circle cx="9.5" cy="9.5" r="8.5"/>
      <ellipse cx="9.5" cy="9.5" rx="4" ry="8.5"/>
      <path d="M9.5 1 V18 M1 9.5 H18 M2.5 5 H16.5 M2.5 14 H16.5"/>
    </svg>
    <p class="detail" style="left:24px;top:227px">www.tandemwellbeing.com.au</p>
  </div>
</section>

<section class="card card--back" aria-label="Business card back">
  <svg class="icon" style="left:186px;top:58px" width="33" height="33" viewBox="0 0 33 33" aria-hidden="true">
    <circle cx="16.5" cy="16.5" r="14.5" stroke-width="3"/>
    <path d="M16.5 9 V17.5 H22" stroke-width="2.4"/>
  </svg>
  <p class="appointments-title">Appointment Times</p>
  <div class="appointment-line" style="top:114px"></div>
  <div class="appointment-line" style="top:143px"></div>
  <div class="appointment-line" style="top:172px"></div>
  <div class="appointment-line" style="top:201px"></div>
  <div class="appointment-line" style="top:229px"></div>
</section>

</body>
</html>
```